Land Buying Company Needs Letterhead for Direct Mail Marketing to Land Owners

We are looking for a professional letterhead that we will be including in our direct mail marketing. We will be sending this to land owners who may be interested in selling or purchasing land.

The letterhead needs to be editable. Headers and footers would look nice, but we are open. We would want it to include our address, website, phone, and email info. For right now the address to use for design purposes would the following:

Address: 415 Bramwell Avenue #600
Dallas, TX 75219
Website - www.quillridgeacres.example
Email - info@quillridgeacres.example
Phone - 866-402-ACRE

I have attached our logo zip file that we just had done on Pixel Guild. Let me know what questions you have, and thank you.

```html
<!DOCTYPE html>
<html lang="en">
<head>
<meta charset="utf-8">
<title>Quillridge Acres Letterhead</title>
<link rel="stylesheet" href="https://fonts.googleapis.com/css2?family=Montserrat:wght@700&family=Lato:wght@400;700&display=swap">
<style>
  :root {
    --backdrop: #cbcbcb;
    --paper: #ffffff;
    --forest: #4a6528;
    --leaf: #8cc43f;
    --mist: #e3e2dd;
    --ink-light: #ffffff;
  }
  * { margin: 0; padding: 0; box-sizing: border-box; }
  html, body {
    width: 1200px;
    height: 1200px;
    overflow: hidden;
    background: var(--backdrop);
  }
  .letterhead {
    position: absolute;
    left: 175px;
    top: 50px;
    width: 850px;
    height: 1100px;
    background: var(--paper);
    box-shadow: 0 4px 18px rgba(0,0,0,0.18);
    overflow: hidden;
  }
  .brand {
    position: absolute;
    left: 70px;
    top: 70px;
    display: flex;
    align-items: center;
    gap: 16px;
  }
  .brand-dot {
    width: 62px;
    height: 62px;
    border-radius: 50%;
    background: var(--forest);
    flex: none;
  }
  .brand-name {
    font-family: "Montserrat", sans-serif;
    font-weight: 700;
    font-size: 38px;
    letter-spacing: 1px;
    text-transform: uppercase;
    color: var(--leaf);
    line-height: 1;
  }
  .watermark {
    position: absolute;
    left: 265px;
    top: 330px;
    width: 420px;
    height: 420px;
    border-radius: 50%;
    background: var(--mist);
  }
  .contact-line {
    position: absolute;
    left: 70px;
    right: 70px;
    bottom: 86px;
    font-family: "Lato", sans-serif;
    font-weight: 700;
    font-size: 15px;
    letter-spacing: 0.6px;
    color: var(--leaf);
    text-align: left;
  }
  .contact-line .divider {
    color: var(--forest);
    margin: 0 8px;
  }
  .footer-band {
    position: absolute;
    left: 0;
    right: 0;
    bottom: 0;
    height: 66px;
    background: var(--forest);
    display: flex;
    align-items: center;
    padding-left: 160px;
  }
  .address {
    font-family: "Lato", sans-serif;
    font-weight: 700;
    font-size: 20px;
    letter-spacing: 1px;
    color: var(--ink-light);
  }
</style>
</head>
<body>
  <main class="letterhead">
    <header class="brand">
      <span class="brand-dot"></span>
      <span class="brand-name">Quillridge Acres</span>
    </header>

    <div class="watermark" aria-hidden="true"></div>

    <footer>
      <p class="contact-line">
        866-402-ACRE<span class="divider">|</span>info@quillridgeacres.example<span class="divider">|</span>www.quillridgeacres.example
      </p>
      <div class="footer-band">
        <p class="address">415 Bramwell Avenue #600 Dallas, TX 75219</p>
      </div>
    </footer>
  </main>
</body>
</html>
```